Golden Years Wellness Roadmap: This is my second book. The first was Eldercare Compass

I need a book cover design for: GOLDEN YEARS WELLNESS ROADMAP: A NO-EXPENSE METHOD FOR FINISHING YOUR LATER-LIFE MOSAIC WITH POOLED KVB CARE SCHEMES by Derek Holloway Neil Osgrove & Martin Quarles. This book is designed for business owners, CEO's, CFO's and Human Resources. The cover needs to be professional and focused on business. The purpose of this book is to educate business owners and their management about a zero cost retiree health plan. This is a first of it's kind solution that every business needs to learn about.

Target Market(s)

Business owners, CEO's, CFO's and Human Resources

Requirements
Nice to have
• I want the design to be clean and professional since it is focused on business executives

```html
<!DOCTYPE html>
<html lang="en">
<head>
<meta charset="utf-8">
<title>Golden Years Wellness Roadmap – Book Cover</title>
<link rel="stylesheet" href="https://fonts.googleapis.com/css2?family=Bebas+Neue&family=Oswald:wght@300&display=swap">
<style>
  :root {
    --stage: #2a2420;
    --navy-deep: #0b1a2e;
    --navy: #14284a;
    --navy-light: #1d3a60;
    --gold: #c9a13a;
    --gold-light: #e8c766;
    --ink-white: #ffffff;
  }
  * { margin: 0; padding: 0; box-sizing: border-box; }
  html, body {
    width: 1200px;
    height: 554px;
    overflow: hidden;
    background: var(--stage);
  }
  .stage {
    width: 1200px;
    height: 554px;
    display: flex;
    justify-content: center;
    align-items: center;
  }
  .book-cover {
    position: relative;
    width: 369px;
    height: 554px;
    overflow: hidden;
    color: var(--ink-white);
    text-align: center;
  }
  .cover-texture {
    position: absolute;
    inset: 0;
    background:
      radial-gradient(ellipse at 30% 20%, var(--navy-light) 0%, transparent 55%),
      radial-gradient(ellipse at 75% 75%, var(--navy) 0%, transparent 60%),
      linear-gradient(160deg, var(--navy) 0%, var(--navy-deep) 100%);
  }
  .cover-emblem {
    position: absolute;
    left: 123px;
    top: 50px;
    width: 122px;
    height: 105px;
    background: linear-gradient(135deg, var(--gold-light), var(--gold));
    opacity: 0.85;
  }
  .cover-title {
    position: absolute;
    left: 0;
    right: 0;
    top: 208px;
    font-family: "Bebas Neue", "Oswald", sans-serif;
    font-weight: 400;
    text-transform: uppercase;
    white-space: nowrap;
    line-height: 51px;
    letter-spacing: 0.5px;
  }
  .cover-title .line-one { display: block; font-size: 56px; }
  .cover-title .line-two { display: block; font-size: 56px; }
  .title-rule {
    position: absolute;
    left: 30px;
    right: 29px;
    top: 321px;
    height: 3px;
    background: linear-gradient(90deg, var(--gold), var(--gold-light), var(--gold));
  }
  .cover-subtitle {
    position: absolute;
    left: 22px;
    right: 22px;
    top: 334px;
    font-family: "Oswald", sans-serif;
    font-weight: 300;
    font-size: 14px;
    line-height: 19px;
    text-transform: uppercase;
  }
  .cover-authors {
    position: absolute;
    left: 0;
    right: 0;
    top: 502px;
    font-family: "Oswald", sans-serif;
    font-weight: 300;
    font-size: 14px;
    line-height: 17px;
    text-transform: uppercase;
  }
</style>
</head>
<body>
  <main class="stage">
    <section class="book-cover">
      <div class="cover-texture" role="img" aria-label="Deep navy marble texture with fine gold veins"></div>
      <div class="cover-emblem" role="img" aria-label="Gold emblem of a blueprint scroll with interlocking puzzle pieces"></div>
      <h1 class="cover-title">
        <span class="line-one">Golden Years</span>
        <span class="line-two">Wellness Roadmap</span>
      </h1>
      <div class="title-rule"></div>
      <p class="cover-subtitle">A no-expense method for finishing your later-life mosaic with pooled KVB care schemes</p>
      <p class="cover-authors">By Derek Holloway<br>Neil Osgrove &amp; Martin Quarles</p>
    </section>
  </main>
</body>
</html>
```